kestrova business cards

Hey design gurus!
I'm after a clean, modern, stylish business card for my about to be launched company.
I've uploaded the logos for my company "Kestrova Electrical Solutions"
and also the tarrow alliance logo to whom i am associated.

```html
<!DOCTYPE html>
<html lang="en">
<head>
<meta charset="utf-8">
<title>Kestrova Electrical Solutions – Business Cards</title>
<link rel="stylesheet" href="https://fonts.googleapis.com/css2?family=Open+Sans:wght@400;600;700&display=swap">
<style>
  :root {
    --stage: #222223;
    --card-dark: #1d1d20;
    --card-blue: #2491d3;
    --brand-blue: #1f7fcc;
    --ink-light: #f2f2f2;
    --ink-muted: #cfd3d8;
    --badge-rust: #a5584a;
    --emboss: #26262a;
  }
  * { box-sizing: border-box; margin: 0; padding: 0; }
  html, body {
    width: 1200px; height: 780px; overflow: hidden;
    background: var(--stage);
    font-family: "Open Sans", Arial, sans-serif;
  }
  .stage {
    position: relative; width: 1200px; height: 780px;
    display: flex; align-items: center; justify-content: center; gap: 40px;
  }
  .card {
    position: relative; width: 520px; height: 297px;
    border-radius: 3px; overflow: hidden;
    box-shadow: 0 14px 30px rgba(0,0,0,.45);
  }
  .card--front { background: var(--card-dark); color: var(--ink-light); }
  .card--back  { background: var(--card-blue); display: flex; align-items: center; justify-content: center; }

  .brand { display: flex; align-items: center; gap: 10px; }
  .brand__mark { width: 30px; height: 30px; border-radius: 50%; background: var(--brand-blue); flex: none; }
  .brand__name { font-weight: 700; font-size: 15px; letter-spacing: .04em; color: var(--brand-blue); text-transform: uppercase; white-space: nowrap; }
  .card--front .brand { position: absolute; top: 26px; left: 150px; }
  .card--back .brand__mark { width: 56px; height: 56px; background: #1a6fb6; }
  .card--back .brand__name { font-size: 24px; color: #e8f3fb; }

  .person { position: absolute; top: 86px; left: 38px; padding-left: 14px; border-left: 6px solid var(--brand-blue); }
  .person__name { font-size: 26px; font-weight: 700; line-height: 1.1; }
  .person__first { color: var(--brand-blue); }
  .person__role { font-size: 14px; color: var(--ink-muted); margin-top: 2px; }

  .address { position: absolute; top: 160px; left: 58px; font-size: 13px; line-height: 1.4; color: var(--ink-light); font-style: normal; }
  .contacts { position: absolute; top: 208px; left: 40px; list-style: none; font-size: 13px; line-height: 1.55; }
  .contacts li { display: flex; align-items: center; gap: 8px; }
  .contacts svg { width: 12px; height: 12px; fill: var(--brand-blue); flex: none; }

  .partner-badge {
    position: absolute; top: 110px; right: 34px; width: 150px; height: 62px;
    border: 1.5px solid var(--badge-rust); border-radius: 8px;
    display: flex; align-items: center; padding-left: 12px;
  }
  .partner-badge__shape { width: 36px; height: 36px; background: var(--badge-rust); border-radius: 4px; }

  .deco-circle {
    position: absolute; right: -40px; bottom: -120px; width: 260px; height: 260px;
    border-radius: 50%; background: var(--emboss);
    box-shadow: inset 0 2px 6px rgba(255,255,255,.05);
  }
</style>
</head>
<body>
<main class="stage">
  <section class="card card--front" aria-label="Business card front">
    <div class="deco-circle"></div>
    <div class="brand">
      <span class="brand__mark"></span>
      <span class="brand__name">Kestrova Electrical Solutions</span>
    </div>
    <div class="person">
      <p class="person__name"><span class="person__first">Mirela</span> Voskova</p>
      <p class="person__role">Managing Director</p>
    </div>
    <address class="address">1840 Lindenhall Ave. Suite 310<br>Denton, TX 76201</address>
    <ul class="contacts">
      <li><svg viewBox="0 0 24 24"><path d="M6.6 10.8a15.1 15.1 0 0 0 6.6 6.6l2.2-2.2a1 1 0 0 1 1-.25 11.4 11.4 0 0 0 3.6.57 1 1 0 0 1 1 1V20a1 1 0 0 1-1 1A17 17 0 0 1 3 4a1 1 0 0 1 1-1h3.5a1 1 0 0 1 1 1c0 1.25.2 2.45.57 3.6a1 1 0 0 1-.25 1z"/></svg>(940) 555-0184</li>
      <li><svg viewBox="0 0 24 24"><path d="M2 5h20v14H2zm2 2v.5l8 5 8-5V7zm0 2.8V17h16V9.8l-8 5z"/></svg>info@kestrova-es.com</li>
      <li><svg viewBox="0 0 24 24"><circle cx="12" cy="12" r="10"/></svg>www.kestrova-es.com</li>
    </ul>
    <div class="partner-badge" aria-label="Tarrow Alliance partner badge">
      <span class="partner-badge__shape"></span>
    </div>
  </section>

  <section class="card card--back" aria-label="Business card back">
    <div class="brand">
      <span class="brand__mark"></span>
      <span class="brand__name">Kestrova Electrical Solutions</span>
    </div>
  </section>
</main>
</body>
</html>
```